Communication Business Card Design

We offer complete cabling solutions
Data Cabling,Fibre Optic, and Cabling Repairs fault finding
Security camera installation
TV Aerial installation
Security alarm installation
QWV

Industry/Entity Type

Business

Contact Information for Business Card

Threadmore Solutions
ABN 52 918 374 260
EMAIL threadmoresolutions.com.au
Mobile 0418362057
Rob Kesler

```html
<!DOCTYPE html>
<html lang="en">
<head>
<meta charset="utf-8">
<title>Threadmore Solutions – Business Cards</title>
<link href="https://fonts.googleapis.com/css2?family=Questrial&family=Exo+2:wght@700&display=swap" rel="stylesheet">
<style>
  :root{
    --bg:#e9eaec;
    --card:#ffffff;
    --navy:#0d1a8c;
    --blue:#1b34b8;
    --ink:#2a2a2a;
    --grey:#9a9a9a;
    --faint:#f1f2f2;
  }
  html,body{margin:0;padding:0;overflow:hidden}
  body{width:1200px;height:1001px;background:var(--bg);position:relative;font-family:"Questrial",sans-serif;color:var(--ink)}
  .card{position:absolute;width:449px;height:251px;border-radius:11px;overflow:hidden;background:var(--card);box-shadow:0 2px 6px rgba(0,0,0,.12)}
  .card--front{left:263px;top:78px}
  .card--back{left:362px;top:375px;width:450px;background:linear-gradient(125deg,#1a2f9e 0%,#2a47c4 45%,#1c35ad 70%,#2443bf 100%)}
  .card--alt{left:487px;top:672px}
  .faint-circle{position:absolute;border-radius:50%;background:var(--faint)}
  .brand{position:absolute;display:flex;align-items:center;gap:9px}
  .brand__dot{width:52px;height:52px;border-radius:50%;background:var(--navy);flex:none}
  .brand__name{line-height:1;color:var(--ink)}
  .brand__main{display:block;font-size:24px;letter-spacing:.2px}
  .brand__sub{display:block;font-size:13px;letter-spacing:.6px;margin-top:1px}
  .brand--light .brand__dot{width:61px;height:61px;background:#fff}
  .brand--light .brand__name{color:#fff}
  .brand--light .brand__main{font-size:29px}
  .brand--light .brand__sub{font-size:16px}
  .person{position:absolute;line-height:1.1}
  .person__name{font-family:"Exo 2",sans-serif;font-weight:700;font-size:14px;color:var(--navy);display:block;letter-spacing:.2px}
  .person__role{font-size:11px;display:block;margin-top:2px}
  .contacts{position:absolute;list-style:none;margin:0;padding:0;font-size:11px;line-height:13.6px}
  .contacts li{display:flex;align-items:center;gap:5px}
  .icon{width:11px;height:10px;flex:none}
  .abn{position:absolute;font-size:11px;margin:0}
  .wave{position:absolute;left:0;bottom:0;width:100%;height:40px}
  .photo{position:absolute;inset:0}
</style>
</head>
<body>

<!-- Front card -->
<section class="card card--front">
  <div class="faint-circle" style="left:243px;top:100px;width:184px;height:184px"></div>
  <div class="brand" style="left:34px;top:33px">
    <span class="brand__dot"></span>
    <span class="brand__name"><span class="brand__main">THREADMORE</span><span class="brand__sub">SOLUTIONS</span></span>
  </div>
  <div class="person" style="right:35px;top:41px;text-align:right">
    <span class="person__name">ROB KESLER</span>
    <span class="person__role">Director</span>
  </div>
  <ul class="contacts" style="left:35px;top:150px">
    <li><svg class="icon" viewBox="0 0 11 10"><rect width="11" height="10" rx="2" fill="var(--navy)"/><path d="M3.5 2.5c-.5 2 1.5 4.5 4 5l.8-1.2-1.4-.8-.6.6c-.8-.4-1.4-1-1.8-1.8l.6-.6-.8-1.4z" fill="#fff"/></svg>0418362057</li>
    <li><svg class="icon" viewBox="0 0 11 10"><rect width="11" height="10" rx="2" fill="var(--navy)"/><rect x="2.5" y="3" width="6" height="4" fill="none" stroke="#fff" stroke-width=".8"/><path d="M2.5 3l3 2.2 3-2.2" fill="none" stroke="#fff" stroke-width=".8"/></svg>info@threadmoresolutions.com.au</li>
    <li><svg class="icon" viewBox="0 0 11 10"><rect width="11" height="10" rx="2" fill="var(--navy)"/><circle cx="5.5" cy="5" r="3" fill="none" stroke="#fff" stroke-width=".7"/><path d="M2.5 5h6M5.5 2v6" stroke="#fff" stroke-width=".6"/></svg>www.threadmoresolutions.com.au</li>
  </ul>
  <p class="abn" style="left:35px;top:201px">ABN 52 918 374 260</p>
  <svg class="wave" viewBox="0 0 449 40" preserveAspectRatio="none">
    <path d="M0 24 Q220 -4 449 26 L449 40 L0 40 Z" fill="var(--grey)"/>
    <path d="M0 29 Q220 2 449 31 L449 40 L0 40 Z" fill="#fff"/>
    <path d="M140 40 Q300 2 420 40 Z" fill="var(--navy)"/>
  </svg>
</section>

<!-- Back card -->
<section class="card card--back">
  <div class="photo" role="img" aria-label="Blue-toned photo of glowing fibre optic strands and network cable connectors"></div>
  <div class="brand brand--light" style="left:102px;top:94px">
    <span class="brand__dot"></span>
    <span class="brand__name"><span class="brand__main">THREADMORE</span><span class="brand__sub">SOLUTIONS</span></span>
  </div>
</section>

<!-- Alternate front card -->
<section class="card card--alt">
  <div class="faint-circle" style="left:269px;top:4px;width:224px;height:224px"></div>
  <div class="brand" style="left:35px;top:33px">
    <span class="brand__dot"></span>
    <span class="brand__name"><span class="brand__main">THREADMORE</span><span class="brand__sub">SOLUTIONS</span></span>
  </div>
  <div class="person" style="left:35px;top:116px">
    <span class="person__name">ROB KESLER</span>
    <span class="person__role">Director</span>
  </div>
  <ul class="contacts" style="left:35px;top:157px">
    <li><svg class="icon" viewBox="0 0 11 10"><rect width="11" height="10" rx="2" fill="var(--navy)"/><path d="M3.5 2.5c-.5 2 1.5 4.5 4 5l.8-1.2-1.4-.8-.6.6c-.8-.4-1.4-1-1.8-1.8l.6-.6-.8-1.4z" fill="#fff"/></svg>0418362057</li>
    <li><svg class="icon" viewBox="0 0 11 10"><rect width="11" height="10" rx="2" fill="var(--navy)"/><rect x="2.5" y="3" width="6" height="4" fill="none" stroke="#fff" stroke-width=".8"/><path d="M2.5 3l3 2.2 3-2.2" fill="none" stroke="#fff" stroke-width=".8"/></svg>info@threadmoresolutions.com.au</li>
    <li><svg class="icon" viewBox="0 0 11 10"><rect width="11" height="10" rx="2" fill="var(--navy)"/><circle cx="5.5" cy="5" r="3" fill="none" stroke="#fff" stroke-width=".7"/><path d="M2.5 5h6M5.5 2v6" stroke="#fff" stroke-width=".6"/></svg>www.threadmoresolutions.com.au</li>
  </ul>
  <p class="abn" style="left:35px;top:207px">ABN 52 918 374 260</p>
  <svg class="wave" viewBox="0 0 449 40" preserveAspectRatio="none">
    <path d="M0 24 Q220 -4 449 26 L449 40 L0 40 Z" fill="var(--grey)"/>
    <path d="M0 29 Q220 2 449 31 L449 40 L0 40 Z" fill="#fff"/>
    <path d="M140 40 Q300 2 420 40 Z" fill="var(--navy)"/>
  </svg>
</section>

</body>
</html>
```